Oven Cleaning Business owner needs business card design

Hi there,
Would like for a business card to be designed for myself, the owner of a professional oven cleaning business on the Sunshine Coast.
Would like it to look sleek, and modern-ish. Bit creative is encouraged too.
Include following:
Name/title: Corin ter Haghe, Owner
Phone number: 1300 482 916
Email: info@hearthshinecrew.com.au
Website: www.hearthshinecrew.com.au

```html
<!DOCTYPE html>
<html lang="en">
<head>
<meta charset="utf-8">
<title>Hearthshine Crew – Business Card</title>
<link href="https://fonts.googleapis.com/css2?family=Poppins:wght@500;600;700&display=swap" rel="stylesheet">
<style>
  :root {
    --backdrop: #e4e5e6;
    --card: #ffffff;
    --ink: #2b2b2d;
    --teal: #4bbcc4;
    --teal-soft: #d8eff1;
    --teal-softer: #eaf6f7;
    --icon-line: #3a3a3c;
  }
  * { margin: 0; padding: 0; box-sizing: border-box; }
  html, body {
    width: 1200px; height: 745px; overflow: hidden;
    background: var(--backdrop);
    font-family: "Poppins", sans-serif;
    color: var(--ink);
  }
  .canvas { position: relative; width: 1200px; height: 745px; }

  .card {
    position: absolute;
    top: 207px;
    width: 560px; height: 330px;
    background: var(--card);
    overflow: hidden;
    box-shadow: 0 10px 28px rgba(0,0,0,0.12);
  }
  .card--front { left: 27px; }
  .card--back { left: 613px; }

  /* Wordmark */
  .wordmark { display: flex; align-items: center; gap: 14px; white-space: nowrap; }
  .wordmark__dot {
    flex: none; border-radius: 50%; background: var(--teal);
  }
  .wordmark__name {
    font-weight: 700; color: var(--ink);
    letter-spacing: 0.02em; line-height: 1;
    text-transform: uppercase;
  }

  .card--front .wordmark {
    position: absolute; left: 50%; top: 50%;
    transform: translate(-50%, -50%);
  }
  .card--front .wordmark__dot { width: 62px; height: 62px; }
  .card--front .wordmark__name { font-size: 32px; }

  /* Back side */
  .back__art {
    position: absolute; right: 0; top: 0;
    width: 190px; height: 330px;
    background: linear-gradient(160deg, var(--teal-softer) 0%, var(--teal-soft) 60%, var(--teal-softer) 100%);
  }
  .card--back .wordmark { position: absolute; left: 30px; top: 46px; gap: 10px; }
  .card--back .wordmark__dot { width: 40px; height: 40px; }
  .card--back .wordmark__name { font-size: 18px; }

  .back__rule {
    position: absolute; left: 30px; top: 104px;
    width: 300px; height: 4px; background: var(--teal);
  }
  .back__dash {
    position: absolute; top: 78px; height: 5px; background: var(--ink);
  }
  .back__dash--long { left: 294px; width: 42px; }
  .back__dash--short { left: 342px; width: 20px; }

  .holder { position: absolute; left: 30px; top: 122px; }
  .holder__name { font-size: 25px; font-weight: 600; line-height: 1.1; letter-spacing: -0.01em; }
  .holder__title { font-size: 11px; font-weight: 500; letter-spacing: 0.04em; margin-top: 2px; }

  .contacts { position: absolute; left: 42px; top: 176px; list-style: none; }
  .contacts__item {
    display: flex; align-items: center; gap: 12px;
    height: 36px; font-size: 17px; font-weight: 500; white-space: nowrap;
  }
  .contacts__icon {
    flex: none; width: 20px; height: 20px;
    border: 1px solid var(--icon-line); border-radius: 50%;
    display: flex; align-items: center; justify-content: center;
  }
  .contacts__icon svg { width: 11px; height: 11px; }
</style>
</head>
<body>
<main class="canvas">

  <section class="card card--front" aria-label="Card front">
    <div class="wordmark">
      <span class="wordmark__dot"></span>
      <span class="wordmark__name">Hearthshine Crew</span>
    </div>
  </section>

  <section class="card card--back" aria-label="Card back">
    <div class="back__art" role="img" aria-label="Large faint illustration of a water droplet with an oven and sparkles"></div>

    <div class="wordmark">
      <span class="wordmark__dot"></span>
      <span class="wordmark__name">Hearthshine Crew</span>
    </div>
    <span class="back__dash back__dash--long"></span>
    <span class="back__dash back__dash--short"></span>
    <div class="back__rule"></div>

    <div class="holder">
      <p class="holder__name">Corin ter Haghe</p>
      <p class="holder__title">OWNER</p>
    </div>

    <ul class="contacts">
      <li class="contacts__item">
        <span class="contacts__icon">
          <svg viewBox="0 0 24 24" fill="none" stroke="#3a3a3c" stroke-width="2.4" stroke-linejoin="round"><path d="M5 3h4l2 5-2.5 1.5a11 11 0 0 0 6 6L16 13l5 2v4a2 2 0 0 1-2 2A17 17 0 0 1 3 5a2 2 0 0 1 2-2z"/></svg>
        </span>
        <span>1300 482 916</span>
      </li>
      <li class="contacts__item">
        <span class="contacts__icon">
          <svg viewBox="0 0 24 24" fill="none" stroke="#3a3a3c" stroke-width="2.4" stroke-linejoin="round"><rect x="3" y="5" width="18" height="14"/><path d="M3 5l9 8 9-8"/></svg>
        </span>
        <span>info@hearthshinecrew.com.au</span>
      </li>
      <li class="contacts__item">
        <span class="contacts__icon">
          <svg viewBox="0 0 24 24" fill="none" stroke="#3a3a3c" stroke-width="2.2"><circle cx="12" cy="12" r="9"/><path d="M3 12h18M12 3c3 3 3 15 0 18M12 3c-3 3-3 15 0 18"/></svg>
        </span>
        <span>www.hearthshinecrew.com.au</span>
      </li>
    </ul>
  </section>

</main>
</body>
</html>
```